Road Construction Company needs business cards

We would like a new business card designed for our business.

We're a road construction company based in Qld, Australia.

Can the business card please have the following information on it.

Name: Brent Malvoy
Position: General Manager
Phone: 0471 592 304
Email: Brent.malvoy@quendix.com.au
Address: 87 Harrowgate Ave, Pindarra, QLD, 4000
Website: www.quendix.com.au

Visually we'd like the card to be professional and simple.

Attached is our logo.

Our website is www.quendix.com.au

Target Market(s)

Men aged 25-60

Contact Information for Business Card

As listed in project description

Font styles to use
Serif

Requirements
Must have
• Large logo on back of card

```html
<!DOCTYPE html>
<html lang="en">
<head>
<meta charset="utf-8">
<title>Quendix Business Card</title>
<link rel="stylesheet" href="https://fonts.googleapis.com/css2?family=Cormorant+Garamond:wght@500;600&display=swap">
<style>
  :root {
    --page-bg: #d9d9d9;
    --card-bg: #000000;
    --brand-blue: #1f7fd1;
    --text-blue: #2a8ad6;
    --rule-blue: #1762c2;
  }
  * { margin: 0; padding: 0; box-sizing: border-box; }
  html, body {
    width: 1200px;
    height: 822px;
    overflow: hidden;
    background: var(--page-bg);
  }
  .canvas {
    position: relative;
    width: 1200px;
    height: 822px;
    font-family: "Cormorant Garamond", Georgia, serif;
    font-variant-numeric: lining-nums;
  }
  .card {
    position: absolute;
    top: 289px;
    width: 389px;
    height: 251px;
    background: var(--card-bg);
  }
  .card--front { left: 164px; }
  .card--back { left: 640px; }

  .brand-name {
    position: absolute;
    left: 0;
    right: 0;
    top: 104px;
    text-align: center;
    font-size: 36px;
    font-weight: 600;
    letter-spacing: 4px;
    line-height: 1;
    color: var(--brand-blue);
  }

  .person {
    position: absolute;
    right: 229px;
    top: 113px;
    text-align: right;
    white-space: nowrap;
    color: var(--text-blue);
  }
  .person__name {
    font-size: 12.5px;
    font-weight: 600;
    letter-spacing: 2.6px;
    line-height: 1;
    margin-right: -2.6px;
  }
  .person__role {
    margin-top: 7px;
    margin-right: -2.2px;
    font-size: 9px;
    font-weight: 500;
    letter-spacing: 2.2px;
    line-height: 1;
  }

  .contact-rule {
    position: absolute;
    left: 189px;
    top: 92px;
  }
  .contact {
    position: absolute;
    left: 209px;
    white-space: nowrap;
    color: var(--text-blue);
    font-size: 11.5px;
    font-weight: 500;
    line-height: 12px;
  }
  .contact--phone { top: 89px; }
  .contact--email { top: 108px; }
  .contact--address { top: 126px; }
  .contact--web { top: 158px; }
</style>
</head>
<body>
<main class="canvas">
  <section class="card card--front" aria-label="Card front">
    <div class="brand-name">QUENDIX</div>
  </section>

  <section class="card card--back" aria-label="Card back">
    <div class="person">
      <p class="person__name">BRENT MALVOY</p>
      <p class="person__role">GENERAL MANAGER</p>
    </div>

    <svg class="contact-rule" width="10" height="74" viewBox="0 0 10 74" aria-hidden="true">
      <line x1="5" y1="3" x2="5" y2="71" stroke="var(--rule-blue)" stroke-width="1"/>
      <circle cx="5" cy="3" r="2.8" fill="var(--rule-blue)"/>
      <circle cx="5" cy="22" r="2.8" fill="var(--rule-blue)"/>
      <circle cx="5" cy="40" r="2.8" fill="var(--rule-blue)"/>
      <circle cx="5" cy="71" r="2.8" fill="var(--rule-blue)"/>
    </svg>

    <p class="contact contact--phone">0471 592 304</p>
    <p class="contact contact--email">brent.malvoy@quendix.com.au</p>
    <p class="contact contact--address">87 Harrowgate Ave, Pindarra,<br>QLD, 4000</p>
    <p class="contact contact--web">www.quendix.com.au</p>
  </section>
</main>
</body>
</html>
```